Calvera fine stockings - sexy cardboard box design needed!

We need a packaging design for a new online company based in Sydney called 'Calvera Hosiery'. We will be selling sexy stockings to our customers by Italian designers. We mainly feature lace stockings, an example of which, can be seen here:
http://www.brindelatessuti.example/italy-FASHION-WINTER

The design should be a cardboard pull out box, black in colour with the logo on the cover. We are looking for the logo to communicate sophistication and sexiness.

Examples of cardboard box shapes we would like are:
http://www.tradovex.example/product-gs/583016294/High_quality_drawer_paper_box.html

http://www.tradovex.example/product-gs/536192047/Cardboard_drawer_box.html

29 December:
I submitted a note when I extended the deadline, but cannot see it, so will write here for clarification. It has been difficult to choose the best design as the designs submitted were of such high quality. I want to have some people judge the designs, but because of the Christmas Season I have extended the deadline so that this can be done. Thanks.

Target Market(s)

The working professional woman.

Industry/Entity Type

Fashion

Requirements
Must have
• The words "Calvera Hosiery" on the cover of the box.

The box should be a sliding drawer.

The box size should be: (22*15*2.5cm).

Washing instructions and recycling logos on the back of the box. See example of uploaded file.

Nice to have
• It would be nice to have the background of the box a dark colour, maybe charcoal? But we are open to all ideas.
Should not have
• A stock photo on cover of box.

```html
<!DOCTYPE html>
<html lang="en">
<head>
<meta charset="utf-8">
<title>Calvera Hosiery — drawer box artwork</title>
<link rel="stylesheet" href="https://fonts.googleapis.com/css2?family=Josefin+Sans:wght@400&display=swap">
<style>
  :root {
    --board: #abb3a0;
    --lid-black: #0c0c0c;
    --wine: #850000;
    --wine-deep: #6e0000;
    --ink: #020205;
    --gold-light: #fff25a;
    --gold: #e6d200;
    --gold-dark: #8a7800;
    --logo: #ffffff;
  }
  html, body {
    margin: 0;
    padding: 0;
    overflow: hidden;
  }
  body {
    width: 1200px;
    height: 818px;
    background: var(--board);
    position: relative;
  }
  .side-flap {
    position: absolute;
    top: 0;
    width: 1200px;
    height: 818px;
    left: 0;
  }
  .sleeve {
    position: absolute;
    left: 237px;
    top: 95px;
    width: 723px;
    height: 468px;
  }
  .sleeve-cover {
    position: absolute;
    inset: 0 0 131px 0;
    background: radial-gradient(ellipse at 50% 60%, #141414 0%, var(--lid-black) 70%);
    box-shadow: inset 0 8px 6px -6px #3a3a3a;
  }
  .brand-name {
    position: absolute;
    left: 0;
    right: 0;
    top: 256px;
    text-align: center;
    margin: 0;
    font-family: "Josefin Sans", sans-serif;
    font-weight: 400;
    font-size: 19px;
    letter-spacing: 2px;
    color: var(--logo);
    text-transform: lowercase;
  }
  .gold-rail {
    position: absolute;
    left: 0;
    right: 0;
    top: 336px;
    height: 9px;
    border-radius: 4px;
    background: linear-gradient(to bottom, var(--gold-light) 0%, var(--gold) 45%, var(--gold-dark) 100%);
  }
  .sleeve-band {
    position: absolute;
    left: 0;
    right: 0;
    bottom: 0;
    height: 122px;
    background: var(--wine);
  }
  .drawer-front {
    position: absolute;
    left: 237px;
    top: 605px;
    width: 723px;
    height: 116px;
    background: var(--wine);
  }
  .drawer-pull {
    position: absolute;
    left: 323px;
    top: 38px;
    width: 80px;
    height: 52px;
  }
</style>
</head>
<body>
  <svg class="side-flap" viewBox="0 0 1200 818" aria-hidden="true">
    <defs>
      <linearGradient id="pull-gold" x1="0" y1="0" x2="0" y2="1">
        <stop offset="0" stop-color="#fff25a"/>
        <stop offset="0.5" stop-color="#e6d200"/>
        <stop offset="1" stop-color="#8a7800"/>
      </linearGradient>
    </defs>
    <g class="flap-left">
      <path d="M75 100 C150 210 205 380 188 563 L75 531 Z" fill="var(--wine)"/>
      <path d="M75 100 L133 487 L75 531 Z" fill="var(--ink)"/>
    </g>
    <g class="flap-right">
      <path d="M1122 100 C1047 210 993 380 1010 563 L1123 531 Z" fill="var(--wine)"/>
      <path d="M1122 100 L1064 487 L1123 531 Z" fill="var(--ink)"/>
    </g>
  </svg>

  <section class="sleeve">
    <div class="sleeve-cover" role="img" aria-label="Charcoal lid with a faint tonal repeat pattern"></div>
    <p class="brand-name">calvera hosiery</p>
    <div class="gold-rail"></div>
    <div class="sleeve-band"></div>
  </section>

  <section class="drawer-front">
    <svg class="drawer-pull" viewBox="0 0 80 52" aria-hidden="true">
      <path d="M18 14 L40 50 L62 14 Z" fill="#6b4a00"/>
      <path d="M22 14 L40 42 L58 14 Z" fill="url(#pull-gold)"/>
      <rect x="0" y="0" width="80" height="14" rx="7" fill="url(#pull-gold)"/>
    </svg>
  </section>
</body>
</html>
```